Cobalt Ridge Mini Storage - Ad for half Page

Need half page ad for a publication.
would also like to be able to use in the future
self storage facility - 3 locations, the third opening soon
do not like real busy projects...i have a logo but willing to tweak if needed

```html
<!DOCTYPE html>
<html lang="en">
<head>
<meta charset="utf-8">
<title>Cobalt Ridge Mini Storage – Half Page Ad</title>
<link rel="stylesheet" href="https://fonts.googleapis.com/css2?family=Montserrat:wght@400;500;700;800;900&display=swap">
<style>
  :root {
    --orange: #ff6a13;
    --brown: #5b2e12;
    --ink: #222222;
    --charcoal: #3d3d3d;
    --icon: #4a4a4a;
    --white: #ffffff;
    --panel-light: #fbfbfb;
    --panel-edge: #d2d2d2;
    --kraft: #c69a68;
    --kraft-dark: #8a6440;
  }
  * { box-sizing: border-box; margin: 0; padding: 0; }
  html, body { width: 854px; height: 1200px; overflow: hidden; background: var(--white); }
  body { font-family: "Montserrat", sans-serif; color: var(--ink); }
  .ad { position: relative; width: 854px; height: 1200px; overflow: hidden; background: var(--white); }

  .ad-panel {
    position: absolute; left: 0; top: 430px; width: 854px; height: 674px;
    background: radial-gradient(ellipse 70% 60% at 45% 40%, var(--panel-light) 0%, #ececec 60%, var(--panel-edge) 100%);
  }
  .hero-photo {
    position: absolute; left: 0; top: 110px; width: 854px; height: 320px;
    background: linear-gradient(180deg, rgba(255,255,255,0) 0%, var(--kraft) 28%, #b8885a 70%, var(--kraft-dark) 100%);
  }

  .brand { position: absolute; left: 48px; top: 38px; display: flex; align-items: center; gap: 12px; }
  .brand-mark { width: 62px; height: 62px; background: var(--brown); }
  .brand-name { font-weight: 800; font-size: 25px; line-height: 29px; color: var(--brown); letter-spacing: 0.2px; }

  .contact { position: absolute; right: 28px; top: 48px; text-align: right; font-size: 17px; line-height: 32px; color: #3a3a3a; }
  .contact-row { display: flex; justify-content: flex-end; align-items: center; gap: 8px; }
  .contact-row svg { width: 12px; height: 12px; }

  .headline {
    position: absolute; left: 40px; top: 330px;
    font-weight: 900; font-size: 122px; line-height: 113px; letter-spacing: -2px;
    color: var(--orange); text-transform: uppercase;
    text-shadow: 6px 5px 0 var(--white);
  }

  .intro { position: absolute; left: 48px; top: 695px; width: 640px; font-size: 17.5px; line-height: 25px; color: var(--ink); }

  .unit-type { position: absolute; left: 48px; display: flex; align-items: center; gap: 26px; }
  .unit-type.climate { top: 830px; }
  .unit-type.standard { top: 948px; }
  .unit-type svg { width: 100px; height: 74px; }
  .unit-label { font-weight: 800; font-size: 28px; line-height: 29px; color: var(--ink); }

  .features { position: absolute; left: 550px; top: 820px; list-style: none; }
  .features li { display: flex; align-items: center; gap: 18px; font-size: 17.5px; line-height: 31px; color: #2b2b2b; }
  .features svg { width: 17px; height: 17px; flex: none; }

  .locations-tab {
    position: absolute; left: 222px; top: 1060px; width: 410px; height: 46px;
    background: var(--charcoal); border-radius: 30px 30px 0 0;
    color: var(--white); font-weight: 700; font-size: 22px; text-align: center; line-height: 48px;
  }
  .locations-band { position: absolute; left: 0; top: 1104px; width: 854px; height: 96px; background: var(--charcoal); display: flex; justify-content: space-between; padding: 22px 40px 0 46px; color: var(--white); }
  .location { text-align: center; }
  .location-city { font-size: 17.5px; line-height: 24px; }
  .location-phone { font-weight: 700; font-size: 23px; line-height: 30px; display: flex; align-items: center; gap: 4px; justify-content: center; }
  .location-phone svg { width: 16px; height: 16px; }
</style>
</head>
<body>
<div class="ad">
  <div class="ad-panel"></div>
  <div class="hero-photo" role="img" aria-label="Photo of a huge pile of cardboard moving boxes with one hand reaching up out of the pile"></div>

  <div class="brand">
    <div class="brand-mark"></div>
    <div class="brand-name">Cobalt Ridge<br>Mini Storage</div>
  </div>

  <div class="contact">
    <div class="contact-row">sales@CobaltRidgeMiniStorage.com
      <svg viewBox="0 0 12 12"><rect x="0.5" y="2" width="11" height="8" fill="#3a3a3a"/><path d="M1 2.5 6 6.5 11 2.5" stroke="#fff" fill="none"/></svg></div>
    <div class="contact-row">www.CobaltRidgeMiniStorage.com
      <svg viewBox="0 0 12 12"><circle cx="6" cy="6" r="5.5" fill="#3a3a3a"/><path d="M0.5 6h11M6 0.5c-3 3-3 8 0 11M6 0.5c3 3 3 8 0 11" stroke="#fff" stroke-width="0.8" fill="none"/></svg></div>
  </div>

  <h1 class="headline">Need a<br>Storage<br>Unit?</h1>

  <p class="intro">We are a family-owned, premier self-storage facility located in San Antonio and New Braunfels. We offer solutions to your Personal Storage, Business Storage and RV &amp; Boat Storage needs.</p>

  <div class="unit-type climate">
    <svg viewBox="0 0 100 74">
      <path d="M2 18 42 2 82 18v6H76v48H8V24H2z" fill="var(--icon)"/>
      <rect x="16" y="28" width="52" height="44" fill="#e8e8e8"/>
      <g stroke="var(--icon)" stroke-width="2.5"><line x1="16" y1="36" x2="68" y2="36"/><line x1="16" y1="44" x2="68" y2="44"/><line x1="16" y1="52" x2="68" y2="52"/><line x1="16" y1="60" x2="68" y2="60"/></g>
      <rect x="74" y="6" width="16" height="52" rx="8" fill="#fff" stroke="var(--icon)" stroke-width="3"/>
      <circle cx="82" cy="62" r="10" fill="#fff" stroke="var(--icon)" stroke-width="3"/>
      <rect x="79.5" y="22" width="5" height="40" fill="var(--icon)"/><circle cx="82" cy="62" r="6" fill="var(--icon)"/>
      <g stroke="var(--icon)" stroke-width="1.5"><line x1="92" y1="14" x2="98" y2="14"/><line x1="92" y1="22" x2="98" y2="22"/><line x1="92" y1="30" x2="98" y2="30"/><line x1="92" y1="38" x2="98" y2="38"/><line x1="92" y1="46" x2="98" y2="46"/></g>
    </svg>
    <div class="unit-label">Climate<br>Controlled<br>Units</div>
  </div>

  <div class="unit-type standard">
    <svg viewBox="0 0 100 74">
      <path d="M2 18 47 2 92 18v6H84v48H10V24H2z" fill="var(--icon)"/>
      <rect x="22" y="30" width="50" height="42" fill="#e8e8e8"/>
      <g stroke="var(--icon)" stroke-width="2.5"><line x1="22" y1="38" x2="72" y2="38"/><line x1="22" y1="46" x2="72" y2="46"/><line x1="22" y1="54" x2="72" y2="54"/><line x1="22" y1="62" x2="72" y2="62"/></g>
    </svg>
    <div class="unit-label">Non-Climate<br>Units</div>
  </div>

  <ul class="features">
    <li><svg viewBox="0 0 17 17"><rect width="17" height="17" rx="3" fill="var(--icon)"/><path d="M4 8.5 7.3 11.8 13 5.5" stroke="#fff" stroke-width="2.2" fill="none"/></svg>Safe &amp; Secure Units</li>
    <li><svg viewBox="0 0 17 17"><rect width="17" height="17" rx="3" fill="var(--icon)"/><path d="M4 8.5 7.3 11.8 13 5.5" stroke="#fff" stroke-width="2.2" fill="none"/></svg>Friendly &amp; Professional Staff</li>
    <li><svg viewBox="0 0 17 17"><rect width="17" height="17" rx="3" fill="var(--icon)"/><path d="M4 8.5 7.3 11.8 13 5.5" stroke="#fff" stroke-width="2.2" fill="none"/></svg>Electronic Gate Access</li>
    <li><svg viewBox="0 0 17 17"><rect width="17" height="17" rx="3" fill="var(--icon)"/><path d="M4 8.5 7.3 11.8 13 5.5" stroke="#fff" stroke-width="2.2" fill="none"/></svg>Online Account Access</li>
    <li><svg viewBox="0 0 17 17"><rect width="17" height="17" rx="3" fill="var(--icon)"/><path d="M4 8.5 7.3 11.8 13 5.5" stroke="#fff" stroke-width="2.2" fill="none"/></svg>No Deposit Required</li>
    <li><svg viewBox="0 0 17 17"><rect width="17" height="17" rx="3" fill="var(--icon)"/><path d="M4 8.5 7.3 11.8 13 5.5" stroke="#fff" stroke-width="2.2" fill="none"/></svg>Month-to-month Rentals</li>
    <li><svg viewBox="0 0 17 17"><rect width="17" height="17" rx="3" fill="var(--icon)"/><path d="M4 8.5 7.3 11.8 13 5.5" stroke="#fff" stroke-width="2.2" fill="none"/></svg>Security Camera Monitoring</li>
  </ul>

  <div class="locations-tab">3 CONVENIENT LOCATIONS</div>
  <div class="locations-band">
    <div class="location">
      <div class="location-city">San Antonio</div>
      <div class="location-phone"><svg viewBox="0 0 16 16"><path d="M3 1.5 6 4.5 4.5 6.5c1 2 3 4 5 5L11.5 10l3 3-2 2C7 14.5 1.5 9 1 3.5z" fill="#fff"/></svg>210-555-0147</div>
    </div>
    <div class="location">
      <div class="location-city">New Braunfels</div>
      <div class="location-phone"><svg viewBox="0 0 16 16"><path d="M3 1.5 6 4.5 4.5 6.5c1 2 3 4 5 5L11.5 10l3 3-2 2C7 14.5 1.5 9 1 3.5z" fill="#fff"/></svg>830-555-0192</div>
    </div>
    <div class="location">
      <div class="location-city">Converse @ IH10</div>
      <div class="location-phone">COMING SOON!</div>
    </div>
  </div>
</div>
</body>
</html>
```